Kelvar Systems Website

Website design for our company: Kelvar Systems.
The website should look fresh and IT focused. Please have a look at http://www.kelvarsystems.net.au/ for our current design. We want something fresh and new, professional looking, in WordPress so we can easily make changes.

Industry/Entity Type

It Company

```html
<!DOCTYPE html>
<html lang="en">
<head>
<meta charset="utf-8">
<title>Kelvar Systems</title>
<link rel="stylesheet" href="https://fonts.googleapis.com/css2?family=Open+Sans:ital,wght@0,400;0,600;0,700;1,700&display=swap">
<style>
:root{
  --green:#00b04f;
  --green-dark:#009a43;
  --blue:#0a78c8;
  --blue-tile:#0e86dc;
  --tile-line:#4fb0f0;
  --charcoal:#333038;
  --charcoal-top:#2b2a2f;
  --bubble:#5c5a61;
  --white:#ffffff;
  --ink:#3a3a3a;
  --heading-blue:#1a78c2;
}
*{box-sizing:border-box;margin:0;padding:0}
html,body{width:1200px;height:2338px;overflow:hidden}
body{font-family:"Open Sans",Arial,sans-serif;color:var(--ink);background:var(--white);position:relative}
.ip-bar{height:39px;background:var(--charcoal-top);color:#ddd;font-size:14px;text-align:center;line-height:39px}
.site-header{height:84px;background:var(--green);position:relative}
.brand{position:absolute;left:70px;top:8px;display:flex;align-items:center;gap:18px}
.brand-dot{width:104px;height:84px;border-radius:50%;background:var(--white)}
.brand-name{color:var(--white);font-weight:700;font-size:26px}
.main-nav{position:absolute;right:66px;top:0;height:84px;display:flex;align-items:center;gap:26px}
.main-nav a{color:var(--white);font-weight:700;font-size:15px;text-decoration:none}
.hero{height:442px;position:relative;background:linear-gradient(100deg,#c9d8e4 0%,#9fb7cc 30%,#6b8aa6 55%,#2d3f55 78%,#1d2a3b 100%)}
.search{position:absolute;left:249px;top:169px;width:706px;height:63px;background:rgba(255,255,255,.92);border:5px solid rgba(210,214,220,.9);display:flex;align-items:center;padding:0 18px}
.search span{font-size:26px;font-weight:700;color:#333;flex:1}
.search-mode{position:absolute;left:249px;top:243px;display:flex;gap:52px;color:var(--white);font-size:15px;font-weight:600}
.search-mode label{display:flex;align-items:center;gap:10px}
.radio{width:22px;height:22px;border-radius:50%;background:#ddd;border:2px solid #999;display:inline-flex;align-items:center;justify-content:center}
.radio.on::after{content:"";width:10px;height:10px;border-radius:50%;background:#555}
.welcome{height:136px;background:var(--green);color:var(--white);text-align:center;padding-top:26px}
.welcome h1{font-size:27px;font-weight:700}
.welcome p{font-size:15.5px;margin-top:8px}
.mission{height:443px;position:relative}
.mission-copy{position:absolute;left:101px;top:48px;width:570px}
.mission h2{color:var(--heading-blue);font-size:27px;font-weight:700;margin-bottom:14px}
.mission p{font-size:15.5px;line-height:1.42;margin-bottom:22px}
.director{position:absolute;left:107px;top:283px;display:flex;align-items:center;gap:18px}
.avatar{width:88px;height:88px;border-radius:50%;background:radial-gradient(circle at 50% 40%,#c99a7c,#5a4334)}
.director-name{font-weight:700;font-style:italic;font-size:15.5px;line-height:1.25}
.remote{position:absolute;left:707px;top:43px;width:425px;height:253px;background:linear-gradient(90deg,#6f7a84,#8c969f 60%,#a5adb4)}
.remote h3{color:var(--white);text-align:center;font-size:27px;font-weight:700;margin-top:26px}
.code-input{margin:24px auto 0;width:360px;height:52px;background:#e8e8e8;border:4px solid #b9bec3;font-size:15px;color:#555;padding:12px 14px}
.connect{display:block;margin:18px auto 0;width:162px;height:44px;background:var(--green);color:var(--white);font-weight:700;font-size:15px;text-align:center;line-height:44px;border-radius:3px}
.services{height:401px;background:linear-gradient(180deg,#0a6fc0,#0b7fd3);position:relative}
.services h2{color:var(--white);text-align:center;font-size:27px;font-weight:700;padding-top:32px}
.tile{position:absolute;width:242px;height:113px;background:var(--blue-tile);border:1px solid var(--tile-line);color:var(--white);text-align:center;font-weight:700;font-size:15px}
.tile svg{display:block;margin:18px auto 10px;width:36px;height:36px}
.tile.active{background:var(--charcoal);border-color:var(--charcoal)}
.testimonials{height:532px;background:var(--charcoal);position:relative;color:var(--white)}
.testimonials h2{text-align:center;font-size:27px;font-weight:700;padding-top:44px}
.quote{position:absolute;background:var(--bubble);font-size:15.5px;line-height:1.42;padding:22px 28px}
.quote::after{content:"";position:absolute;left:40px;bottom:-22px;border-left:0 solid transparent;border-right:22px solid transparent;border-top:22px solid var(--bubble)}
.quote p+p{margin-top:22px}
.cite{position:absolute;font-size:13px;color:#ddd}
.site-footer{height:261px;background:var(--green);color:var(--white);text-align:center}
.site-footer .lead{font-size:15px;padding-top:42px}
.partners{display:flex;justify-content:center;gap:36px;margin-top:20px}
.partners+.partners{margin-top:18px}
.badge{width:130px;height:44px;background:rgba(255,255,255,.88);border-radius:6px}
.badge.round{width:56px;border-radius:50%}
.footer-rule{width:466px;height:1px;background:rgba(255,255,255,.35);margin:28px auto 0}
.copyright{font-size:13.5px;margin-top:12px;color:#e6f7ec}
</style>
</head>
<body>
<div class="ip-bar">Your IP address is 127.0.0.1 which resolves to xxx.yyy.xxx.255</div>

<header class="site-header">
  <div class="brand"><span class="brand-dot"></span><span class="brand-name">Kelvar Systems</span></div>
  <nav class="main-nav">
    <a href="#">HOME</a><a href="#">CLIENTS</a><a href="#">SERVICES</a><a href="#">SUPPORT AREAS</a><a href="#">ABOUT US</a><a href="#">CONTACT US</a>
  </nav>
</header>

<section class="hero" role="img" aria-label="Smiling technician connecting cables in a server rack">
  <div class="search"><span>Search...</span>
    <svg width="26" height="26" viewBox="0 0 24 24" fill="none" stroke="#333" stroke-width="3"><circle cx="10" cy="10" r="7"/><path d="M15 15l7 7"/></svg>
  </div>
  <div class="search-mode">
    <label><span class="radio on"></span>LOCAL</label>
    <label><span class="radio"></span>WEB</label>
  </div>
</section>

<section class="welcome">
  <h1>Welcome to Kelvar Systems</h1>
  <p>Kelvar Systems is an Adelaide based company with a single objective - to excel in the support and service of all computer and IT needs.</p>
</section>

<section class="mission">
  <div class="mission-copy">
    <h2>Our Mission</h2>
    <p>We provide a high level of consulting services using the most experienced engineers at a reasonable and fair price. We believe in using a Business Value approach to every aspect of computer consulting to provide our clients with the most cost effective solutions.</p>
    <p>We strongly believe that we are in business with our clients. Each thing we do must be measured against our clients' business objectives. At the end of the day our client's success is our success.</p>
  </div>
  <div class="director">
    <div class="avatar" role="img" aria-label="Portrait of the managing director"></div>
    <div class="director-name">Daniel Rourke<br>Managing Director</div>
  </div>
  <div class="remote" role="img" aria-label="Support agent wearing a headset">
    <h3>Remote Support</h3>
    <div class="code-input">Enter your 6-digit code</div>
    <span class="connect">CONNECT NOW</span>
  </div>
</section>

<section class="services">
  <h2>Our Services:</h2>
  <div class="tile active" style="left:68px;top:99px"><svg viewBox="0 0 24 24" fill="none" stroke="#fff" stroke-width="1.6"><rect x="6" y="2" width="12" height="20"/><path d="M9 6h2M13 6h2M9 10h2M13 10h2M9 14h2M13 14h2M11 22v-4h2v4"/></svg>On-site Service</div>
  <div class="tile" style="left:343px;top:99px"><svg viewBox="0 0 24 24" fill="#fff"><circle cx="12" cy="7" r="4"/><path d="M4 22c0-5 4-8 8-8s8 3 8 8z"/></svg>Medical IT Service</div>
  <div class="tile" style="left:618px;top:99px"><svg viewBox="0 0 24 24" fill="none" stroke="#fff" stroke-width="1.8"><rect x="3" y="5" width="15" height="15" rx="2"/><path d="M10 14l1-3 9-9 2 2-9 9z"/></svg>Website Design</div>
  <div class="tile" style="left:892px;top:99px"><svg viewBox="0 0 24 24" fill="#fff"><rect x="1" y="6" width="14" height="11"/><path d="M15 9h4l4 4v4h-8z"/><circle cx="6" cy="18" r="2.5"/><circle cx="18" cy="18" r="2.5"/></svg>Hardware / Software supply</div>
  <div class="tile" style="left:68px;top:243px"><svg viewBox="0 0 24 24" fill="none" stroke="#fff" stroke-width="1.8"><rect x="2" y="3" width="20" height="14"/><path d="M8 21h8M12 17v4"/></svg>Remote Desktop Support</div>
  <div class="tile" style="left:343px;top:243px"><svg viewBox="0 0 24 24" fill="#fff"><path d="M9 3h6v3h-6z" fill="none" stroke="#fff" stroke-width="1.6"/><rect x="2" y="6" width="20" height="15" rx="2"/><path d="M11 9h2v3h3v2h-3v3h-2v-3H8v-2h3z" fill="#0e86dc"/></svg>Pharmacy IT Service</div>
  <div class="tile" style="left:618px;top:243px"><svg viewBox="0 0 24 24" fill="none" stroke="#fff" stroke-width="2.2"><circle cx="12" cy="12" r="9"/><circle cx="12" cy="12" r="4"/><path d="M5.6 5.6l3.6 3.6M18.4 5.6l-3.6 3.6M5.6 18.4l3.6-3.6M18.4 18.4l-3.6-3.6"/></svg>Disaster Recovery</div>
  <div class="tile" style="left:892px;top:243px"><svg viewBox="0 0 24 24" fill="#fff" stroke="#0e86dc" stroke-width="0.8"><path d="M12 2l6 3v6l-6 3-6-3V5z"/><path d="M6 11l6 3v7l-6-3zM18 11l-6 3v7l6-3z"/><path d="M1 13l5-2v7l-5 2zM23 13l-5-2v7l5 2z"/></svg>Consumables</div>
</section>

<section class="testimonials">
  <h2>What do our clients say about Kelvar?</h2>
  <div class="quote" style="left:68px;top:119px;width:517px;height:319px">
    <p>“I have used Kelvar Systems as a primary supplier of hardware &amp; computer support for the last 5 years, at both the Harlow &amp; Penrice and the Verrani Pharmacy groups, where I have been employed as an I.T. Coordinator/Support Officer. Owen &amp; his team are always friendly, prompt &amp; conscientious. They have an excellent wealth of knowledge &amp; I.T. savvy, always willing to ‘go the extra mile’ to get the job done.</p>
    <p>Their excellent knowledge of all POS systems is nice to know, to get you out of all sorts of problem situations. Not only that, someone is always contactable from Kelvar Systems, no matter what time of the day.”</p>
  </div>
  <div class="cite" style="left:141px;top:466px">Marcus Ellwood B.Pharm AACPA Corwin Chemists, Hillford</div>
  <div class="quote" style="left:618px;top:119px;width:514px;height:167px">
    <p>“I have always found the team extremely helpful with their advice over the phone. They also have the ability to access our computers remotely, and can rectify most problems quite swiftly. I have no hesitation in recommending Kelvar Systems for all of your IT needs.”</p>
  </div>
  <div class="cite" style="left:695px;top:303px">Glen Asher (Harlow &amp; Penrice Pharmacy Group)</div>
</section>

<footer class="site-footer">
  <p class="lead">Kelvar is proudly partnered with the following vendors:</p>
  <div class="partners">
    <span class="badge"></span><span class="badge"></span><span class="badge round"></span><span class="badge round"></span>
  </div>
  <div class="partners">
    <span class="badge" style="width:92px"></span><span class="badge"></span>
  </div>
  <div class="footer-rule"></div>
  <p class="copyright">Copyright © 2014 Kelvar Systems Pty Ltd. All Rights Reserved.</p>
</footer>
</body>
</html>
```